Fitness Centre/Personal Trainer Business Card

We need a business card design for a company based in Singapore called 'Vigor Summit'.

We are a team of Personal Trainers and we are planning to open our new training facility.

This design will also be printed/painted on the walls in our gym.

We are a new breed of personal trainers who take fitness seriously and holistically. We do not merely train our clients to be big and muscular.

We believe in wholeness. In our opinion, fitness should include: strength, speed, flexibility, mobility, stamina & agility. These are what we train for. Of course, nutrition/diet is key.

We use fitness tools such as kettlebells, QLV, Pylometric boxes, battling ropes, clubbells, medicine balls, bulgarian bags etc - functional and non-bulky tools.

I currently have a Facebook page 'Vigor Summit SG' which shows a logo of a kettlebell. But my business focus has since changed.

Services provided:
- Kettlebell Sport Preparation
- Calisthenics Training
- Corrective Exercises
- Sports Strength & Conditioning
- 28 days Weight Loss Program
- Myofascial Rehab Therapy
- Sports/Thai Massage

Main colors for the design should be BLACK & YELLOW. We envision a design which is able to protray the holistic view we take on fitness. Also it should somewhat appeal to the ladies and not intimidate them.

Target Market(s)

People between 18-35 years old. Students and working class alike.

Industry/Entity Type

Training

Requirements
Must have
• Name: Marcus Oleander Pryce
Fitness Coach
Corrective Exercise Specialist
M: +65 9372 6058
E: marcus@sgvigorsummit-example.com

Double-sided please.
Nice to have
• "What is your vigor summit?"

```html
<!DOCTYPE html>
<html lang="en">
<head>
<meta charset="utf-8">
<title>Vigor Summit – Business Card</title>
<link rel="stylesheet" href="https://fonts.googleapis.com/css2?family=Open+Sans:wght@400;600;700&display=swap">
<style>
  :root{
    --yellow:#f7d117;
    --black:#0a0a0a;
    --ink:#1c1c1c;
    --grey-line:#9a9a9a;
    --stage:#cfcfcf;
    --stage-light:#ececec;
    --card-border:#b5b5b5;
    --white:#ffffff;
  }
  *{box-sizing:border-box;margin:0;padding:0}
  html,body{width:1200px;height:719px;overflow:hidden}
  body{
    position:relative;
    font-family:"Open Sans",Arial,sans-serif;
    background:radial-gradient(ellipse at 50% 40%,var(--stage-light) 0%,var(--stage) 75%);
    color:var(--ink);
  }
  .card{position:absolute;width:539px;height:307px;overflow:hidden}

  /* Front */
  .card--front{left:316px;top:37px;background:var(--white)}
  .card--front .band-top{position:absolute;left:0;top:0;width:100%;height:8px;background:var(--yellow)}
  .card--front .band-bottom{position:absolute;left:0;bottom:0;width:100%;height:8px;background:var(--black)}
  .brand{position:absolute;display:flex;flex-direction:column;align-items:center;gap:12px;text-align:center}
  .brand__dot{width:96px;height:96px;border-radius:50%;background:var(--yellow)}
  .brand__name{font-weight:700;font-size:26px;line-height:1.1}
  .card--front .brand{left:52px;top:70px;width:150px}
  .card--front .brand__name{color:var(--ink)}
  .divider{position:absolute;left:248px;top:65px;width:1px;height:180px;background:var(--grey-line)}
  .contact{position:absolute;left:271px;top:71px}
  .contact__name{font-weight:700;font-size:19.5px;line-height:26px}
  .contact__role{font-size:15px;line-height:20.5px}
  .contact__lines{margin-top:21px;list-style:none}
  .contact__lines li{display:flex;align-items:center;gap:6px;font-size:15px;line-height:24.5px}
  .contact__lines svg{width:11px;height:11px;flex:none}

  /* Back, dark */
  .card--back-dark{left:49px;top:376px;background:var(--black)}
  .card--back-dark .brand{left:55px;top:60px;width:150px}
  .card--back-dark .brand__name{color:var(--yellow)}
  .services{position:absolute}
  .services__title{font-weight:700;font-size:19px}
  .card--back-dark .services{left:276px;top:16px;color:var(--yellow)}
  .card--back-dark .services__list{list-style:none;margin-top:14px}
  .card--back-dark .services__list li{font-size:15.5px;line-height:26.6px}
  .services__list li::before{content:"\2022";margin-right:4px}
  .tagline{position:absolute;left:0;width:100%;text-align:center;font-weight:700;font-size:17px;letter-spacing:.4px}
  .card--back-dark .tagline{top:252px;color:var(--white)}

  /* Back, light */
  .card--back-light{left:615px;top:376px;background:var(--white);border:1px solid var(--card-border)}
  .ghost-mark{position:absolute;left:180px;top:20px;width:178px;font-weight:700;font-size:34px;color:var(--yellow);opacity:.14;text-align:center;line-height:1.1;padding-top:40px}
  .card--back-light .services{left:0;top:62px;width:100%;text-align:center}
  .card--back-light .services__list{list-style:none;margin-top:14px;display:flex;flex-direction:column;align-items:center}
  .card--back-light .services__list li{font-size:17px;line-height:32.5px;white-space:nowrap}
  .card--back-light .services__list li span + span{margin-left:8px}
  .card--back-light .services__list li span::before{content:"\2022";margin-right:4px}
  .card--back-light .services__list li::before{content:none}
  .card--back-light .tagline{top:254px;text-transform:uppercase}
</style>
</head>
<body>

<section class="card card--front" aria-label="Card front">
  <div class="band-top"></div>
  <div class="brand">
    <div class="brand__dot"></div>
    <div class="brand__name">Vigor Summit</div>
  </div>
  <div class="divider"></div>
  <div class="contact">
    <p class="contact__name">Marcus Oleander Pryce</p>
    <p class="contact__role">Fitness Coach</p>
    <p class="contact__role">Corrective Exercise Specialist</p>
    <ul class="contact__lines">
      <li><svg viewBox="0 0 12 12" aria-hidden="true"><rect x="3" y="0.5" width="6" height="11" rx="1" fill="none" stroke="#333" stroke-width="1.2"/><rect x="4.3" y="2" width="3.4" height="4" fill="#333"/></svg>+65 9372 6058</li>
      <li><svg viewBox="0 0 12 12" aria-hidden="true"><rect x="0.5" y="2.5" width="11" height="7.5" fill="#333"/><path d="M0.5 2.5 L6 7 L11.5 2.5" fill="none" stroke="#fff" stroke-width="1"/></svg>marcus@sgvigorsummit-example.com</li>
      <li><svg viewBox="0 0 12 12" aria-hidden="true"><circle cx="6" cy="6" r="5.2" fill="none" stroke="#333" stroke-width="1.1"/><ellipse cx="6" cy="6" rx="2.2" ry="5.2" fill="none" stroke="#333" stroke-width="0.9"/><line x1="0.8" y1="6" x2="11.2" y2="6" stroke="#333" stroke-width="0.9"/></svg>www.sgvigorsummit-example.com</li>
    </ul>
  </div>
  <div class="band-bottom"></div>
</section>

<section class="card card--back-dark" aria-label="Card back, dark version">
  <div class="brand">
    <div class="brand__dot"></div>
    <div class="brand__name">Vigor Summit</div>
  </div>
  <div class="services">
    <h2 class="services__title">Services</h2>
    <ul class="services__list">
      <li>Sports Strength &amp; Conditioning</li>
      <li>Kettlebell Sport Preparation</li>
      <li>28 days Weight Loss Program</li>
      <li>Myofascial Rehab Therapy</li>
      <li>Calisthenics Training</li>
      <li>Corrective Exercises</li>
      <li>Sports/Thai Massage</li>
    </ul>
  </div>
  <p class="tagline">What is your vigor summit?</p>
</section>

<section class="card card--back-light" aria-label="Card back, light version">
  <div class="ghost-mark" aria-hidden="true">Vigor Summit</div>
  <div class="services">
    <h2 class="services__title">Services</h2>
    <ul class="services__list">
      <li><span>Sports Strength &amp; Conditioning</span><span>Sports/Thai Massage</span></li>
      <li><span>Kettlebell Sport Preparation</span><span>Corrective Exercises</span></li>
      <li><span>28 days Weight Loss Program</span><span>Calisthenics Training</span></li>
      <li><span>Myofascial Rehab Therapy</span></li>
    </ul>
  </div>
  <p class="tagline">What is your vigor summit?</p>
</section>

</body>
</html>
```